Lidia Vanta Catering
Complete Stationery Design
Lidia Vanta Catering - Chef / Catering
Creative Brief
Bright & Fun-filled
Corazon Belmiro
Director, Sales & Marketing
2nd Floor, Quintero Bldg., Saldivar Avenue near corner Lupine Street, Navotas, Metro Manila, Philippines 1490
cbelmiro@lidiavanta-example.ph
www.lidiavanta-example.ph
Lidia Vanta is a high end catering company. Our design is modern Victorian. Color dark red, black and white but we are open to other color suggestion. We need the ff: - business cards - A4 and letter size paper with matching letter envelopes - Folder that fits A4 and letter size envelop - Fax Cover - CD sticker and cover - Sticker label - Address Sticker Label - Paper Bag Design - Styro lunch box design - Tissue Napkin Design - Name Plate - Identification Card Design
Victorian design with our Logo in the middle

```html
<!DOCTYPE html>
<html lang="en">
<head>
<meta charset="utf-8">
<title>Lidia Vanta Catering — Stationery</title>
<link href="https://fonts.googleapis.com/css2?family=Cormorant+Garamond:ital,wght@0,500;1,500&display=swap" rel="stylesheet">
<style>
  :root{
    --stage:#3b3b3b;
    --paper:#ffffff;
    --paper-shade:#ececec;
    --red:#c4161c;
    --red-dark:#8e0f12;
    --ink:#1a1a1a;
    --muted:#777777;
    --silver:#d9d9d9;
  }
  *{margin:0;padding:0;box-sizing:border-box}
  html,body{width:1200px;height:310px;overflow:hidden;background:var(--stage)}
  body{position:relative;font-family:"Cormorant Garamond",Georgia,serif;color:var(--ink)}
  .piece{position:absolute;background:var(--paper);overflow:hidden;box-shadow:0 1px 3px rgba(0,0,0,.45)}
  .wave{position:absolute;left:0;bottom:0;width:100%;display:block}
  .brand{font-style:italic;font-weight:500;white-space:nowrap;line-height:1}
  .tiny{font-size:4px;line-height:1.35;color:var(--muted);font-style:normal}

  /* presentation mark */
  .hero-brand{position:absolute;left:12px;top:18px;width:132px;text-align:center}
  .hero-brand .brand{font-size:30px;color:var(--silver)}
  .hero-brand .concept{margin-top:14px;font-size:8px;color:var(--silver);letter-spacing:.5px}

  /* business cards */
  .card{width:128px;height:70px}
  .card-front-a{left:12px;top:140px}
  .card-back-a{left:150px;top:140px}
  .card-logo{left:12px;top:228px}
  .card-red{left:150px;top:228px;background:var(--red)}
  .card .brand{position:absolute;font-size:13px;color:var(--ink)}
  .card-front-a .brand{left:8px;top:10px}
  .card-front-a .details{position:absolute;left:64px;top:10px;width:60px}
  .card-back-a .details{position:absolute;left:8px;top:8px;width:112px}
  .card-logo .brand,.card-red .brand{left:0;right:0;top:26px;text-align:center;font-size:15px}
  .card-red .brand{color:var(--paper)}
  .card .name{font-size:6px;color:var(--ink);font-weight:500}

  /* letterheads */
  .letterhead{width:155px;height:288px;top:17px}
  .letterhead-a{left:319px}
  .letterhead-b{left:487px}
  .letterhead .brand{position:absolute;left:12px;top:14px;font-size:15px}
  .letterhead .contact{position:absolute;right:10px;top:12px;width:62px;text-align:right}
  .letterhead .footer{position:absolute;left:0;right:0;bottom:4px;text-align:center;color:var(--paper)}
  .letterhead-b .brand{left:0;right:0;text-align:center;top:16px}

  /* DL envelopes */
  .envelope{width:216px;height:94px;left:696px}
  .envelope-a{top:42px}
  .envelope-b{top:157px}
  .envelope .brand{position:absolute;left:10px;top:10px;font-size:14px}
  .envelope .return{position:absolute;left:10px;top:28px;width:80px}

  /* envelope backs */
  .back{width:240px;left:948px}
  .back svg{position:absolute;inset:0;width:100%;height:100%}
  .back-black{top:42px;height:84px;background:var(--ink)}
  .back-white{top:126px;height:62px;border-top:1px solid var(--paper-shade)}
  .back-plain{top:189px;height:72px}
  .back .brand{position:absolute;left:0;right:0;text-align:center;font-size:12px}
  .back-black .brand{top:44px;color:var(--paper)}
  .back-white .brand{top:28px;color:var(--ink)}
</style>
</head>
<body>

<div class="hero-brand">
  <div class="brand">Lidia Vanta</div>
  <div class="concept">Stationery Concept</div>
</div>

<!-- business cards -->
<section class="piece card card-front-a">
  <div class="brand">Lidia Vanta</div>
  <div class="details tiny"><div class="name">Corazon Belmiro</div>Director, Sales &amp; Marketing<br>cbelmiro@lidiavanta-example.ph<br>www.lidiavanta-example.ph</div>
  <svg class="wave" viewBox="0 0 128 16" preserveAspectRatio="none" height="16"><path d="M0 8 Q64 -2 128 8 V16 H0Z" fill="var(--red)"/><path d="M0 6 Q64 -4 128 6" stroke="var(--ink)" stroke-width=".8" fill="none"/></svg>
</section>
<section class="piece card card-back-a">
  <div class="details tiny"><div class="name">Corazon Belmiro</div>Director, Sales &amp; Marketing<br>2nd Floor, Quintero Bldg., Saldivar Avenue near corner Lupine Street, Navotas, Metro Manila, Philippines 1490<br>cbelmiro@lidiavanta-example.ph</div>
  <svg class="wave" viewBox="0 0 128 16" preserveAspectRatio="none" height="16"><path d="M0 8 Q64 -2 128 8 V16 H0Z" fill="var(--red)"/><path d="M0 6 Q64 -4 128 6" stroke="var(--ink)" stroke-width=".8" fill="none"/></svg>
</section>
<section class="piece card card-logo"><div class="brand">Lidia Vanta</div></section>
<section class="piece card card-red"><div class="brand">Lidia Vanta</div></section>

<!-- letterheads -->
<section class="piece letterhead letterhead-a">
  <div class="brand">Lidia Vanta</div>
  <div class="contact tiny">2nd Floor, Quintero Bldg., Saldivar Avenue near corner Lupine Street, Navotas, Metro Manila, Philippines 1490<br>cbelmiro@lidiavanta-example.ph</div>
  <svg class="wave" viewBox="0 0 155 26" preserveAspectRatio="none" height="26"><path d="M0 12 Q80 0 155 10 V26 H0Z" fill="var(--red)"/><path d="M0 9 Q80 -3 155 7" stroke="var(--ink)" stroke-width="1.2" fill="none"/></svg>
  <div class="footer tiny" style="color:var(--paper)">www.lidiavanta-example.ph</div>
</section>
<section class="piece letterhead letterhead-b">
  <div class="brand">Lidia Vanta</div>
  <svg class="wave" viewBox="0 0 155 26" preserveAspectRatio="none" height="26"><path d="M0 12 Q80 0 155 10 V26 H0Z" fill="var(--red)"/><path d="M0 9 Q80 -3 155 7" stroke="var(--ink)" stroke-width="1.2" fill="none"/></svg>
  <div class="footer tiny" style="color:var(--paper)">www.lidiavanta-example.ph</div>
</section>

<!-- DL envelopes -->
<section class="piece envelope envelope-a">
  <div class="brand">Lidia Vanta</div>
  <div class="return tiny">2nd Floor, Quintero Bldg., Saldivar Avenue near corner Lupine Street, Navotas, Metro Manila, Philippines 1490</div>
  <svg class="wave" viewBox="0 0 216 16" preserveAspectRatio="none" height="16"><path d="M0 9 Q108 -2 216 9 V16 H0Z" fill="var(--red)"/><path d="M0 7 Q108 -4 216 7" stroke="var(--ink)" stroke-width="1" fill="none"/></svg>
</section>
<section class="piece envelope envelope-b">
  <div class="brand">Lidia Vanta</div>
  <div class="return tiny">2nd Floor, Quintero Bldg., Saldivar Avenue near corner Lupine Street, Navotas, Metro Manila, Philippines 1490</div>
  <svg class="wave" viewBox="0 0 216 16" preserveAspectRatio="none" height="16"><path d="M0 9 Q108 -2 216 9 V16 H0Z" fill="var(--red)"/><path d="M0 7 Q108 -4 216 7" stroke="var(--ink)" stroke-width="1" fill="none"/></svg>
</section>

<!-- envelope backs -->
<section class="piece back back-black">
  <svg viewBox="0 0 240 84" preserveAspectRatio="none"><path d="M0 0 L120 62 L240 0" fill="none" stroke="var(--paper)" stroke-width="1.5"/></svg>
  <div class="brand">Lidia Vanta</div>
</section>
<section class="piece back back-white">
  <svg viewBox="0 0 240 62" preserveAspectRatio="none"><path d="M0 0 L120 44 L240 0" fill="none" stroke="var(--red)" stroke-width="1.5"/></svg>
  <div class="brand">Lidia Vanta</div>
</section>
<section class="piece back back-plain">
  <svg viewBox="0 0 240 72" preserveAspectRatio="none"><path d="M0 0 L120 40 L240 0" fill="none" stroke="var(--silver)" stroke-width="1"/><path d="M0 72 L110 34 M240 72 L130 34" stroke="var(--paper-shade)" stroke-width="1"/></svg>
</section>

</body>
</html>
```